Orbit Lane Website - Enabling Omni channel

Slogan : Enabling Omnichannel Sales

1. Sell products via multiple sale channels
2. Access our technology and services to get your products moving through new channels
3. Customise our mobile and web technology platforms to suit your supply chain.

Slogan: Orbit lane – Innovating new business.

Use the content from these websites to create a new one
http://brovanixhq.example/
http://pellow-studio.example/orbitLane02/

Target Market(s)

Business and Coporations who need mobile and web technology or services to increase product sales within their vertical industry. Our case studies show the industries we have worked in; namely: Retail, wholesale, online retail, motor and auto trade. Also have rich experience in Importing and Exporting.

Industry/Entity Type

Retail

Number of Pages Required

3 page

Font styles to use
Sans Serif

Colors
0255a3
ec1f27
9bcb3c
ffffff
0792cd
ffc214

Requirements
Must have
• Punchy headline home page with possible animations or unique and interesting images

```html
<!DOCTYPE html>
<html lang="en">
<head>
<meta charset="utf-8">
<title>Orbit Lane – Innovating new business</title>
<link href="https://fonts.googleapis.com/css2?family=Montserrat:wght@300;400;500;600&family=Open+Sans:wght@400;600&display=swap" rel="stylesheet">
<style>
:root{
  --navy:#0255a3;
  --sky:#0792cd;
  --cyan:#00a8e6;
  --red:#ec1f27;
  --yellow:#ffc214;
  --green:#9bcb3c;
  --white:#ffffff;
  --ink:#333333;
  --muted:#777777;
  --footer:#2b2b2b;
  --footer-bar:#222222;
}
*{box-sizing:border-box;margin:0;padding:0}
html,body{width:1200px;height:3871px;overflow:hidden;background:var(--white)}
body{font-family:"Open Sans",Arial,sans-serif;color:var(--ink);font-size:14px;position:relative}
h1,h2,h3,h4{font-family:"Montserrat",Arial,sans-serif;font-weight:400}

/* header */
.site-header{position:absolute;top:0;left:0;width:1200px;height:78px;background:var(--white);z-index:3}
.brand{position:absolute;left:100px;top:22px;display:flex;align-items:center;gap:8px;font-family:"Montserrat",sans-serif;font-weight:600;font-size:24px;color:var(--navy)}
.brand-dot{width:14px;height:14px;border-radius:50%;background:var(--sky)}
.main-nav{position:absolute;right:98px;top:32px;display:flex;gap:46px}
.main-nav a{font-family:"Montserrat",sans-serif;font-size:11px;color:#444;text-decoration:none;letter-spacing:.3px}

/* hero */
.hero{position:absolute;top:78px;left:0;width:1200px;height:537px;overflow:hidden}
.hero-photo{position:absolute;inset:0;background:
  radial-gradient(ellipse 300px 260px at 560px 170px,rgba(240,214,190,.75),transparent 70%),
  radial-gradient(ellipse 260px 300px at 250px 330px,rgba(90,110,140,.7),transparent 70%),
  radial-gradient(ellipse 300px 320px at 900px 360px,rgba(70,110,170,.65),transparent 70%),
  radial-gradient(ellipse 260px 200px at 1100px 120px,rgba(225,205,170,.6),transparent 70%),
  radial-gradient(ellipse 380px 160px at 600px 500px,rgba(230,232,236,.7),transparent 70%),
  linear-gradient(120deg,#7c8a99 0%,#b9b2a8 40%,#8d9aac 70%,#5f7088 100%)}
.hero-shade{position:absolute;inset:0;background:rgba(20,30,45,.22)}
.hero-copy{position:absolute;top:180px;width:100%;text-align:center;color:var(--white)}
.hero-copy h1{font-size:44px;font-weight:600;line-height:54px}
.hero-copy p{font-family:"Montserrat",sans-serif;font-size:38px;font-weight:300;line-height:48px}
.btn{display:inline-block;background:var(--cyan);color:var(--white);font-family:"Montserrat",sans-serif;font-size:14px;text-decoration:none;border-radius:2px}
.hero-copy .btn{margin-top:22px;padding:13px 30px}

.question-band{position:absolute;top:615px;left:0;width:1200px;height:75px;background:var(--cyan);display:flex;justify-content:center;gap:88px;align-items:center}
.question{display:flex;align-items:center;gap:18px;color:var(--white);font-family:"Montserrat",sans-serif;font-size:16px;font-weight:500}
.question svg{width:38px;height:38px}

/* welcome */
.welcome{position:absolute;top:690px;left:0;width:1200px;text-align:center}
.section-title{font-size:32px;color:#333;padding-top:66px}
.welcome .intro{width:1000px;margin:26px auto 0;font-size:11.5px;line-height:22px;color:var(--muted)}
.features{display:flex;justify-content:space-between;width:1000px;margin:60px auto 0}
.feature{width:260px}
.feature svg{height:100px;width:120px}
.feature h3{font-size:14px;font-weight:500;color:#333;margin-top:16px;line-height:20px;text-transform:uppercase}
.feature p{font-size:11px;color:var(--muted);line-height:20px;margin-top:12px}

/* bundle */
.bundle-head{position:absolute;top:1330px;width:1200px;text-align:center}
.bundle-head h2{font-size:32px}
.bundle-head p{font-size:15px;color:#444;margin-top:18px}
.service{position:absolute;left:100px;width:1000px}
.service .photo{position:absolute}
.service h3{font-size:24px;line-height:36px;color:#333}
.service p.lead{font-size:12px;line-height:24px;color:var(--muted);margin-top:14px}
.service .sub{font-family:"Montserrat",sans-serif;font-size:15px;color:var(--navy);margin-top:10px}
.ticks{list-style:none;margin-top:16px}
.ticks li{font-size:12px;color:var(--muted);line-height:34px;display:flex;align-items:center;gap:12px}
.ticks svg{width:12px;height:12px;flex:none}

/* solutions band */
.solutions{position:absolute;top:2558px;left:0;width:1200px;height:370px;text-align:center;color:var(--white);background:
  radial-gradient(ellipse 420px 200px at 700px 290px,rgba(150,160,175,.45),transparent 70%),
  radial-gradient(ellipse 380px 180px at 520px 120px,rgba(120,130,150,.35),transparent 70%),
  linear-gradient(160deg,#4a5566,#2a313d 55%,#1b2029)}
.solutions h2{font-size:34px;padding-top:118px}
.solutions p{font-size:15px;margin-top:18px;color:#dfe6ee}
.solutions .btn{margin-top:32px;padding:13px 34px}

/* cards */
.cards{position:absolute;top:2980px;left:100px;width:1000px;display:flex;justify-content:space-between}
.card{width:318px}
.card .photo{height:212px}
.card .label{height:40px;padding:0 22px;display:flex;align-items:center;color:var(--white);font-family:"Montserrat",sans-serif;font-weight:500;font-size:15px}
.label.red{background:var(--red)}
.label.yellow{background:var(--yellow)}
.label.green{background:var(--green)}

/* newsletter */
.newsletter{position:absolute;top:3300px;width:1200px;text-align:center}
.newsletter h2{font-size:32px}
.newsletter p{font-size:15px;color:#444;margin-top:14px}
.signup{display:flex;justify-content:center;margin-top:30px}
.signup .field{width:478px;height:40px;border:1px solid #ddd;text-align:left;padding:0 14px;line-height:38px;font-size:12px;color:#999}
.signup .btn{width:135px;height:40px;line-height:40px;text-align:center;font-weight:500}

/* footer */
.site-footer{position:absolute;top:3524px;left:0;width:1200px;height:281px;background:var(--footer);color:#bbb}
.foot-col{position:absolute;top:44px}
.foot-col h4{font-family:"Montserrat",sans-serif;font-size:14px;font-weight:500;color:var(--white)}
.foot-col p,.foot-col li{font-size:11px;line-height:20px;color:#a0a0a0}
.foot-col ul{list-style:none;margin-top:18px}
.foot-col ul li{line-height:26px}
.foot-col .more{color:var(--white);font-size:11px;margin-top:14px;display:block}
.news-item{margin-top:18px}
.contact-row{display:flex;gap:10px;align-items:flex-start;margin-top:8px}
.contact-row svg{width:12px;height:12px;margin-top:4px;flex:none}
.social{display:flex;gap:10px;margin-top:18px}
.social span{width:28px;height:28px;border-radius:50%;background:#7a7a7a}
.foot-bar{position:absolute;top:3805px;left:0;width:1200px;height:66px;background:var(--footer-bar);text-align:center;line-height:66px;font-size:11px;color:#888}
</style>
</head>
<body>

<header class="site-header">
  <div class="brand"><span class="brand-dot"></span>Orbit Lane</div>
  <nav class="main-nav">
    <a href="#">HOME</a><a href="#">ABOUT US</a><a href="#">SERVICES</a><a href="#">SOLUTIONS</a><a href="#">HOW IT WORKS</a><a href="#">NEWS</a><a href="#">CONTACT US</a>
  </nav>
</header>

<section class="hero">
  <div class="hero-photo" role="img" aria-label="Business team gathered around a laptop in a bright office"></div>
  <div class="hero-shade"></div>
  <div class="hero-copy">
    <h1>Orbit Lane</h1>
    <p>Innovating new business</p>
    <a class="btn" href="#">Contact here</a>
  </div>
</section>

<div class="question-band">
  <div class="question">
    <svg viewBox="0 0 40 40" fill="none" stroke="#fff" stroke-width="2"><path d="M6 20 L20 6 H34 V20 L20 34 Z"/><circle cx="27" cy="13" r="2.5"/></svg>
    Are you a brand?
  </div>
  <div class="question">
    <svg viewBox="0 0 40 40" fill="none" stroke="#fff" stroke-width="2"><rect x="6" y="6" width="28" height="28" rx="2"/><path d="M16 6 V14 H24 V6"/></svg>
    Do you have Products...?
  </div>
  <div class="question">
    <svg viewBox="0 0 40 40" fill="none" stroke="#fff" stroke-width="2"><circle cx="20" cy="20" r="16"/><path d="M13 27 L27 13"/><circle cx="14" cy="14" r="2.5"/><circle cx="26" cy="26" r="2.5"/></svg>
    Do you offer a service...?
  </div>
</div>

<section class="welcome">
  <h2 class="section-title">Welcome to Orbit Lane</h2>
  <p class="intro">Fashion apparel brand, Orbit Lane acquired the brand, intellectual property, stock and trading in June 2014. The brand consisted of 80 SKU's and sold off a website. In order to increase the sales, Kessler an American retailer assisted in the exporting of the product. The substantial amount of inventory was sold to Kessler and an ongoing export business was established. Our company embarked on a design phase to establish a new range with the purpose of local sales as well as export sales. The project expanded from being a small business, to being a large, global business.</p>
  <div class="features">
    <div class="feature">
      <svg viewBox="0 0 120 100" fill="none" stroke="#9bcb3c" stroke-width="4"><rect x="4" y="14" width="72" height="50" rx="3"/><path d="M30 64 V78 H50 V64 M22 80 H58"/><rect x="70" y="34" width="26" height="44" rx="3"/><rect x="96" y="26" width="20" height="52" rx="3"/></svg>
      <h3>Technology<br>at your fingertips</h3>
      <p>We've developed a range of solutions that can start revolutionising your business' supply chain process now. Or, we can help you make your custom software application, a reality.</p>
    </div>
    <div class="feature">
      <svg viewBox="0 0 120 100" fill="#ffc214"><circle cx="50" cy="58" r="26"/><circle cx="86" cy="28" r="16"/><circle cx="50" cy="58" r="10" fill="#fff"/><circle cx="86" cy="28" r="6" fill="#fff"/><g><rect x="46" y="24" width="8" height="12"/><rect x="46" y="80" width="8" height="12"/><rect x="16" y="54" width="12" height="8"/><rect x="72" y="54" width="12" height="8"/><rect x="82" y="4" width="8" height="10"/><rect x="82" y="42" width="8" height="10"/><rect x="62" y="24" width="10" height="8"/><rect x="100" y="24" width="10" height="8"/></g></svg>
      <h3>Vantro – ready to<br>work end-to-end automation</h3>
      <p>Increasing sales, streamlining processes, minimising errors and reducing costs are all possibilities when you automate your business using our Vantro platform...</p>
    </div>
    <div class="feature">
      <svg viewBox="0 0 120 100" fill="none" stroke="#0792cd" stroke-width="4"><rect x="30" y="6" width="56" height="86" rx="2"/><path d="M86 20 H96 V86 a6 6 0 0 1 -12 0"/><path d="M40 22 H76 M40 34 H76 M40 46 H76 M40 58 H76 M40 70 H76"/></svg>
      <h3>Features<br>and modules</h3>
      <p>We've developed a range of solutions that can start revolutionising your business' supply chain process now. Or, we can help you make your custom software application, a reality.</p>
    </div>
  </div>
</section>

<div class="bundle-head">
  <h2>Awesome Service Bundle</h2>
  <p>Orbit Lane specializes in Feature-rich Services.</p>
</div>

<section class="service" style="top:1470px;height:245px">
  <div class="photo" role="img" aria-label="Hands joining jigsaw puzzle pieces on a wooden table" style="left:0;top:0;width:440px;height:245px;background:radial-gradient(ellipse 160px 90px at 240px 130px,rgba(235,230,222,.55),transparent 70%),radial-gradient(ellipse 120px 80px at 80px 60px,rgba(214,160,130,.5),transparent 70%),linear-gradient(135deg,#5e3f2a,#9a7252 50%,#4f3423)"></div>
  <div style="position:absolute;left:530px;top:22px;width:470px">
    <h3>Partner With Us To Develop<br>A Custom App</h3>
    <p class="lead">Whether you have an app in mind that needs developing or a business process requiring special attention our 20 plus years experience in start ups, media and retailing means we're the right people to help you bring it to life.</p>
  </div>
</section>

<section class="service" style="top:1790px;height:250px">
  <div style="position:absolute;left:6px;top:22px;width:520px">
    <h3>Incorporate The Latest Hardware Devices<br>And Tags To Boost Business</h3>
    <ul class="ticks">
      <li><svg viewBox="0 0 12 12"><path d="M1 6 L4.5 9.5 L11 2" stroke="#ffc214" stroke-width="2.2" fill="none"/></svg>Beacons – enhance customer's in-store experience (Pomelo)</li>
      <li><svg viewBox="0 0 12 12"><path d="M1 6 L4.5 9.5 L11 2" stroke="#ffc214" stroke-width="2.2" fill="none"/></svg>NFC tags – enhance customer's in-store experience (Northwave)</li>
      <li><svg viewBox="0 0 12 12"><path d="M1 6 L4.5 9.5 L11 2" stroke="#ffc214" stroke-width="2.2" fill="none"/></svg>RFID tags- track global supply chains</li>
      <li><svg viewBox="0 0 12 12"><path d="M1 6 L4.5 9.5 L11 2" stroke="#ffc214" stroke-width="2.2" fill="none"/></svg>Video and movement sensors – for in-store retail insights</li>
    </ul>
  </div>
  <div class="photo" role="img" aria-label="Laptop, tablet, phone and plant on a grey desk" style="left:560px;top:0;width:440px;height:250px;background:radial-gradient(ellipse 120px 70px at 260px 90px,rgba(40,40,44,.6),transparent 70%),radial-gradient(ellipse 60px 50px at 70px 50px,rgba(110,160,70,.55),transparent 70%),radial-gradient(ellipse 110px 50px at 250px 190px,rgba(225,225,228,.5),transparent 70%),linear-gradient(135deg,#5d6166,#84888d 50%,#4e5257)"></div>
</section>

<section class="service" style="top:2140px;height:350px">
  <div class="photo" role="img" aria-label="Website shown on a desktop monitor and a smartphone" style="left:14px;top:0;width:390px;height:350px;background:radial-gradient(ellipse 170px 110px at 230px 120px,rgba(45,48,55,.55),transparent 70%),radial-gradient(ellipse 60px 110px at 45px 250px,rgba(40,42,48,.4),transparent 70%),linear-gradient(180deg,#f1f4f6,#dbe2e7 60%,#eef1f3)"></div>
  <div style="position:absolute;left:496px;top:50px;width:500px">
    <h3 style="font-size:30px">Marketing And Sales</h3>
    <p class="sub">We Go To The Ends Of The Earth To Get Your Products Selling.</p>
    <ul class="ticks">
      <li><svg viewBox="0 0 12 12"><path d="M1 6 L4.5 9.5 L11 2" stroke="#ffc214" stroke-width="2.2" fill="none"/></svg>Broaden Customer reach with multi-channel Marketing.</li>
      <li><svg viewBox="0 0 12 12"><path d="M1 6 L4.5 9.5 L11 2" stroke="#ffc214" stroke-width="2.2" fill="none"/></svg>Be where Customers are by Selling Online and on Mobile.</li>
      <li><svg viewBox="0 0 12 12"><path d="M1 6 L4.5 9.5 L11 2" stroke="#ffc214" stroke-width="2.2" fill="none"/></svg>Be top of your Customer's mind using Loyalty.</li>
    </ul>
  </div>
</section>

<section class="solutions" role="img" aria-label="Hands typing on a laptop keyboard in low light">
  <h2>Solutions</h2>
  <p>Let Us Take Care Of The Selling With One Of Our Ready To Go Solutions : specs</p>
  <a class="btn" href="#">Click here</a>
</section>

<section class="cards">
  <div class="card">
    <div class="photo" role="img" aria-label="Businesswoman working at a desk" style="background:radial-gradient(ellipse 90px 100px at 140px 100px,rgba(60,55,55,.45),transparent 70%),linear-gradient(135deg,#e2ddd5,#b0a392)"></div>
    <div class="label red">Are You Experiencing</div>
  </div>
  <div class="card">
    <div class="photo" role="img" aria-label="Audience applauding at a business meeting" style="background:radial-gradient(ellipse 120px 80px at 160px 150px,rgba(220,200,185,.55),transparent 70%),linear-gradient(135deg,#c9cfd6,#6e7a88)"></div>
    <div class="label yellow">Our Solutions Include</div>
  </div>
  <div class="card">
    <div class="photo" role="img" aria-label="Team discussing work around a computer" style="background:radial-gradient(ellipse 110px 90px at 120px 140px,rgba(70,110,160,.45),transparent 70%),linear-gradient(135deg,#e4e8ec,#8ea0b4)"></div>
    <div class="label green">What To Do Now</div>
  </div>
</section>

<section class="newsletter">
  <h2>Newsletter signup</h2>
  <p>Get our recent updates through your email id</p>
  <div class="signup"><div class="field">Enter your email id</div><a class="btn" href="#">Subscribe</a></div>
</section>

<footer class="site-footer">
  <div class="foot-col" style="left:106px;width:330px">
    <h4>About Orbit Lane</h4>
    <p style="margin-top:18px">Fashion apparel brand, Orbit Lane acquired the brand, intellectual property, stock and trading in June 2014. The brand consisted of 80 SKU's and sold off a website. In order to increase the sales, Kessler an American retailer assisted in the exporting of the product...</p>
    <span class="more">Read more info ›</span>
  </div>
  <div class="foot-col" style="left:474px;width:240px">
    <h4>Latest News</h4>
    <p class="news-item">Lorem ipsum is simply dummy text of the printing and typesetting industry</p>
    <p class="news-item">Lorem ipsum is simply dummy text of the printing and typesetting industry</p>
    <p class="news-item">Lorem ipsum is simply dummy text of the printing and typesetting industry</p>
    <span class="more">View more ›</span>
  </div>
  <div class="foot-col" style="left:768px;width:140px">
    <h4>Welcome</h4>
    <ul><li>About Us</li><li>Services</li><li>Solutions</li><li>How it Works</li><li>News</li><li>Contact Us</li></ul>
  </div>
  <div class="foot-col" style="left:956px;width:170px">
    <h4>Contact Info</h4>
    <div class="contact-row" style="margin-top:18px"><svg viewBox="0 0 12 12"><path d="M6 11 C2 6 2 5 2 4.5 a4 4 0 0 1 8 0 C10 5 10 6 6 11Z" fill="#888"/></svg><p>12 Harlow Court, 9 Fenwick Row, Springfield, USA</p></div>
    <div class="contact-row"><svg viewBox="0 0 12 12"><path d="M2 1 L4.5 1 L5.5 4 L4 5 C5 7 6 8 7 8.5 L8 7 L11 8 L11 10.5 C6 11 1 6 2 1Z" fill="#888"/></svg><p>+00 0 0000 0000</p></div>
    <div class="contact-row"><svg viewBox="0 0 12 12"><rect x="1" y="2.5" width="10" height="7" fill="none" stroke="#888"/><path d="M1 3 L6 7 L11 3" fill="none" stroke="#888"/></svg><p>hello@orbitlane.example</p></div>
    <div class="social"><span></span><span></span><span></span><span></span></div>
  </div>
</footer>
<div class="foot-bar">© 2016. Orbit Lane. All rights reserved</div>

</body>
</html>
```